Poster & Banner for Outback tour company

Poster needed for tour company in the Australian outback. We will need it in an A2 format and if possible a larger banner format as Well please. It needs the Harlow Tours logo but also the other logos (less obvious). It also needs to feature the RoamRater logo (uploaded).

The poster needs a list of the tours we offer as well as some of the pictures uploaded.

List of tours:

- Premium Tour of the Town and the Breakaways $99
- Coober Pedy Highlights Tour $85
- Sunset Breakaways Tour $60
- Underground Noodling Tour $50

Industry/Entity Type

Tour Company

Font styles to use
Serif

Colors

Designer to choose colors to be used in the design.

Requirements
Must have
• Harlow Tours logo/List of tours/

```html
<!DOCTYPE html>
<html lang="en">
<head>
<meta charset="utf-8">
<title>Explore Coober Pedy with Harlow Tours</title>
<link rel="stylesheet" href="https://fonts.googleapis.com/css2?family=Lato:wght@300;700;900&display=swap">
<style>
  :root {
    --navy: #1d4466;
    --white: #ffffff;
    --ink: #1b1b1b;
    --orange: #f29a1f;
    --earth-dark: #7d3f1f;
    --rule: #444444;
    --partner-blue: #2a6fb5;
    --partner-green: #5a9a3a;
    --partner-clay: #b8531e;
  }
  * { box-sizing: border-box; margin: 0; padding: 0; }
  html, body { width: 857px; height: 1200px; overflow: hidden; background: var(--white); }
  body { font-family: 'Lato', sans-serif; }

  .poster {
    position: absolute; left: 11px; top: 11px;
    width: 835px; height: 1178px;
    background: var(--navy);
    overflow: hidden;
  }
  .hero { position: absolute; left: 0; top: 0; width: 835px; height: 600px; }

  .brand-mark {
    position: absolute; left: 620px; top: 47px;
    width: 168px; height: 82px;
    background: var(--white); border-radius: 5px;
    display: flex; align-items: center; justify-content: center; gap: 8px;
    white-space: nowrap;
  }
  .brand-mark .dot { width: 14px; height: 14px; background: var(--earth-dark); }
  .brand-mark .name { font-weight: 900; font-size: 18px; color: var(--earth-dark); text-transform: uppercase; }

  .headline {
    position: absolute; left: 0; top: 398px; width: 835px;
    text-align: center; color: var(--white);
    font-size: 45px; line-height: 62px; font-weight: 300;
    letter-spacing: -0.3px;
  }
  .headline strong { font-weight: 700; }

  .tours {
    position: absolute; left: 22px; top: 590px;
    display: flex; gap: 24px;
  }
  .tour {
    position: relative; width: 178px; height: 356px;
    background: var(--white); border-radius: 89px;
    padding: 11px 11px 0;
  }
  .tour-photo { display: block; width: 156px; height: 165px; border-radius: 78px 78px 18px 18px; }
  .tour-name {
    margin-top: 13px; text-align: center;
    font-weight: 900; font-size: 17px; line-height: 24px; color: var(--ink);
  }
  .tour-price {
    position: absolute; left: 50%; bottom: -13px; transform: translateX(-50%);
    width: 73px; height: 73px; border-radius: 50%;
    background: var(--orange); color: var(--white);
    display: flex; align-items: center; justify-content: center;
    font-weight: 900; font-size: 30px;
  }
  .photo-arch { background: linear-gradient(180deg, #7fa7d4 0%, #c9a27e 70%, #a65a2e 100%); }
  .photo-church { background: linear-gradient(180deg, #c98f5c 0%, #8a3b2a 60%, #3a2a22 100%); }
  .photo-sunset { background: linear-gradient(180deg, #23305a 0%, #6b5b7a 55%, #f08a2c 85%, #1a1a1a 100%); }
  .photo-tunnel { background: linear-gradient(135deg, #9c968c 0%, #6f685f 55%, #3c3630 100%); }

  .partners {
    position: absolute; left: 0; top: 1024px; width: 835px; height: 128px;
    background: var(--white);
    display: flex; align-items: center; justify-content: center;
  }
  .partner {
    display: flex; align-items: center; gap: 8px;
    padding: 0 24px; height: 88px;
    font-weight: 700; font-size: 16px; color: var(--earth-dark);
    white-space: nowrap;
  }
  .partner + .partner { border-left: 1.5px solid var(--rule); }
  .partner .mark-circle { width: 20px; height: 20px; border-radius: 50%; background: currentColor; }
  .partner .mark-square { width: 20px; height: 20px; background: currentColor; }
  .partner.blue { color: var(--partner-blue); }
  .partner.green { color: var(--partner-green); }
  .partner.clay { color: var(--partner-clay); }
</style>
</head>
<body>
<main class="poster">
  <svg class="hero" viewBox="0 0 835 600" role="img" aria-label="Photo of the Breakaways hills under a blue outback sky">
    <defs>
      <linearGradient id="heroFill" x1="0" y1="0" x2="0" y2="1">
        <stop offset="0" stop-color="#1f4f8a"/>
        <stop offset="0.42" stop-color="#7ea6cf"/>
        <stop offset="0.52" stop-color="#d9b58c"/>
        <stop offset="0.7" stop-color="#b4683a"/>
        <stop offset="1" stop-color="#8a4a26"/>
      </linearGradient>
    </defs>
    <path d="M0 0 H835 V440 Q417 706 0 440 Z" fill="url(#heroFill)"/>
  </svg>

  <div class="brand-mark"><span class="dot"></span><span class="name">Harlow Tours</span></div>

  <h1 class="headline">Explore <strong>Coober Pedy</strong> with<br><strong>Harlow Tours</strong></h1>

  <section class="tours">
    <article class="tour">
      <div class="tour-photo photo-arch" role="img" aria-label="Tour bus seen through a rock arch in the desert"></div>
      <h2 class="tour-name">Premium Tour<br>of the Town<br>and the<br>Breakaways</h2>
      <div class="tour-price">$99</div>
    </article>
    <article class="tour">
      <div class="tour-photo photo-church" role="img" aria-label="Underground church with stained glass"></div>
      <h2 class="tour-name">Coober<br>Pedy<br>Highlights<br>Tour</h2>
      <div class="tour-price">$85</div>
    </article>
    <article class="tour">
      <div class="tour-photo photo-sunset" role="img" aria-label="Mining machine silhouetted at sunset"></div>
      <h2 class="tour-name">Sunset<br>Breakaways<br>Tour</h2>
      <div class="tour-price">$60</div>
    </article>
    <article class="tour">
      <div class="tour-photo photo-tunnel" role="img" aria-label="Visitor in an underground mine tunnel"></div>
      <h2 class="tour-name">Underground<br>Noodling<br>Tour</h2>
      <div class="tour-price">$50</div>
    </article>
  </section>

  <footer class="partners">
    <div class="partner"><span class="mark-circle"></span>Redgum Ridge Resort</div>
    <div class="partner blue">Saltbush Parks</div>
    <div class="partner green"><span class="mark-circle"></span>Greenway Villages</div>
    <div class="partner clay"><span class="mark-square"></span>Clay Lodge Motel</div>
  </footer>
</main>
</body>
</html>
```